Tidewell Estates Co Business Card design

Tidewell Estates Co is a West Vancouver based boutique brokerage specializing in the marketing and sale of luxury and waterfront real estate.

This card is for Marlon Prevost, Vice-President.

The card should have something modern and unique about. Some sort of gimmick would be nice.

I would like it to use or update the tidewell estates logo visible at www.tidewellestates.example

Very open to any design.

Target Market(s)

humans, the type with money

Industry/Entity Type

Marketing

Requirements
Must have
• The name Marlon Prevost

Company name Tidewell Estates Co

Phone 604-555-0142

Fax 604-555-0187

email marlonprevost@mailbox.example

website www.marlonprevost.example

LOGO

tag line"a fresh approach to real estate in west vancouver"

the attched pic of me if possible
Nice to have
• Something that would make people say "nice card" and not throw it in the garbage immediately, open to ideas
Should not have
• anything that looks like a template

```html
<!DOCTYPE html>
<html lang="en">
<head>
<meta charset="utf-8">
<title>Tidewell Estates Co — Business Card</title>
<link rel="stylesheet" href="https://fonts.googleapis.com/css2?family=Open+Sans:ital,wght@0,400;0,600;1,400&display=swap">
<style>
  :root {
    --canvas: #ffffff;
    --card-front: #efefef;
    --card-front-light: #fbfbfb;
    --card-back: #4a4a4a;
    --card-back-dark: #3a3a3a;
    --ink: #1a1a1a;
    --ink-soft: #2e2e2e;
    --band: #5c5c5c;
    --band-text: #e6e6e6;
    --portrait-light: #c9bfa8;
    --portrait-dark: #3d3a36;
    --back-brand: #767676;
    --card-shadow: rgba(0, 0, 0, 0.3);
  }
  * { box-sizing: border-box; margin: 0; padding: 0; }
  html, body {
    width: 1200px;
    height: 970px;
    overflow: hidden;
    background: var(--canvas);
    font-family: "Open Sans", Arial, sans-serif;
  }
  .canvas {
    position: relative;
    width: 1200px;
    height: 970px;
  }
  .card {
    position: absolute;
    width: 780px;
    height: 480px;
    overflow: hidden;
    box-shadow: 2px 4px 12px var(--card-shadow);
  }
  .card--front {
    left: 70px;
    top: 55px;
    z-index: 2;
    background: linear-gradient(160deg, var(--card-front-light) 0%, var(--card-front) 40%, var(--card-front-light) 68%, #e6e6e6 100%);
  }
  .card--back {
    left: 330px;
    top: 400px;
    z-index: 1;
    background: linear-gradient(160deg, var(--card-back) 0%, var(--card-back-dark) 55%, var(--card-back) 100%);
  }

  .brand {
    position: absolute;
    left: 305px;
    top: 52px;
    display: flex;
    align-items: center;
    gap: 20px;
  }
  .brand__mark {
    width: 60px;
    height: 60px;
    background: var(--ink);
  }
  .brand__name {
    font-size: 54px;
    line-height: 64px;
    font-weight: 600;
    color: var(--ink);
    letter-spacing: 0.5px;
  }

  .portrait {
    position: absolute;
    left: 22px;
    top: 178px;
    width: 244px;
    height: 302px;
    background: linear-gradient(180deg, var(--card-front) 0%, var(--portrait-light) 40%, var(--portrait-dark) 100%);
  }

  .person {
    position: absolute;
    left: 305px;
    top: 244px;
    font-size: 22px;
    color: var(--ink);
  }
  .person__name { font-weight: 600; }
  .person__title { color: var(--ink-soft); }

  .contact {
    position: absolute;
    left: 305px;
    top: 304px;
    list-style: none;
    font-size: 20px;
    line-height: 28px;
    color: var(--ink-soft);
  }
  .contact__label { color: var(--ink); margin-right: 6px; }

  .tagline-band {
    position: absolute;
    left: 0;
    bottom: 0;
    width: 100%;
    height: 40px;
    background: var(--band);
    opacity: 0.92;
    display: flex;
    align-items: center;
    justify-content: flex-end;
    padding-right: 20px;
  }
  .tagline {
    font-size: 19px;
    font-style: italic;
    color: var(--band-text);
    letter-spacing: 0.3px;
  }

  .back-brand {
    position: absolute;
    right: 44px;
    bottom: 48px;
    display: flex;
    align-items: center;
    gap: 14px;
  }
  .back-brand__mark {
    width: 22px;
    height: 22px;
    background: var(--back-brand);
  }
  .back-brand__name {
    font-size: 32px;
    font-weight: 600;
    color: var(--back-brand);
  }
</style>
</head>
<body>
<main class="canvas">
  <section class="card card--front" aria-label="Business card front">
    <div class="brand">
      <span class="brand__mark"></span>
      <span class="brand__name">Tidewell<br>Estates</span>
    </div>

    <div class="portrait" role="img" aria-label="Portrait photograph of Marlon Prevost in a light jacket"></div>

    <p class="person">
      <span class="person__name">Marlon Prevost</span>
      <span class="person__title">Vice-President</span>
    </p>

    <ul class="contact">
      <li><span class="contact__label">P:</span>604-555-0142</li>
      <li><span class="contact__label">F:</span>604-555-0187</li>
      <li><span class="contact__label">e:</span>marlonprevost@mailbox.example</li>
      <li><span class="contact__label">w:</span>www.marlonprevost.example</li>
    </ul>

    <div class="tagline-band">
      <p class="tagline">"a fresh approach to real estate in west vancouver"</p>
    </div>
  </section>

  <section class="card card--back" aria-label="Business card back">
    <div class="back-brand">
      <span class="back-brand__mark"></span>
      <span class="back-brand__name">Tidewell Estates</span>
    </div>
  </section>
</main>
</body>
</html>
```